Banner ad design for Vantora Display Ads

We are looking for a designer to develop a concept for banner ads for a Vantora Display campaign we are building.

We have 3 business lines, shredding services, records management services and scanning services.

We are looking for 4 sets of ads to be created, one for each business line + one set that showcases all of our lines together.

For the design concepts, we would like to see a few sizes (banner, square, leaderboard, skyscraper, etc) for each.

The person chosen will then need to create the ads into all Vantora supported sizes -- 20 sizes total for each set of ads as per the Vantora size guidelines found on this page - https://help.vantora-example.com/vantora-ads/answer/4827150?hl=en&ref_topic=6604821#

A few items to note:
- Design should complement our existing brand/website look and feel (www.oak-ferry.ca)
- Each final ad must be 150Kb or less in size
- Final designs should be editable, meaning if we would like to change some copy in the design, we can do so using a well-known software (Canva, Photoshop/InDesign, etc)
- Some images are attached for use, but if you feel a different stock image is more suitable to to your design, please go ahead and use it.

Provided below is some messaging that can be used for each set of ads. Do not feel you need to use all of the messaging, it is provided for guidance.

SHREDDING SERVICES:

Possible Short Headline:
-- One-Time Shredding Services
-- Secure Shredding Services
-- Affordable On-Site Shredding

Possible Long Headline
-- Your Paper Can be Destroyed as Soon as the Next Business Day

Possible Descriptions:
-- KVEC Gold Certified On site shredding company. Service as soon as Next Day.
-- Secure and Affordable Toronto & GTA On-Site Shredding.
-- Certified, Affordable Office Shredding Since 2003.
-- Quick, no contact and affordable paper shredding services in Toronto & Southern Ontario.
-- Certified, Affordable Office Shredding Since 2003. Fast, no contact shredding service.

Call to Action
-- Get a Quote

RECORDS MANAGEMENT
Short Headline:
-- Off-site Records Storage
-- Records Management & Storage
-- Secure Records Storage
-- Records Management Services
-- Long Term Records Management
-- Document Storage Solutions

Possible Description
-- Local, Affordable Storage Solutions. Protect and Store your Documents in our Secure Facility
-- Local, Affordable Records Management Solutions. Store your Records in our Secure Facility
-- Certified, Affordable Document Storage Since 2004. Contact Us for a Free Quote!
-- Vaultline+ Certified, Affordable Document Storage Since 2004. Contact Us for a Free Quote!

Call to Action
-- Get a Quote

SCANNING SERVICES

Short Headline:
-- Professional Scanning Company
-- Toronto & GTA Scanning Service
-- Document Scanning Services
-- Digital Conversion Services
-- Fast & Easy Retrieval

Description
-- Scan and documents and files with Professional scanning services from Oak-Ferry
-- Convert Your Paper Files to Electronic Files. Fast & Easy Retrieval.
-- Easily access your documents electronically with Document Scanning Services

Call to Action
-- Get a Quote

ALL SERVICES AD SET
Short Headline
-- Shred, Scan & Store Documents
-- Secure Shredding, Records Management and Scanning Services
-- #1 Document Management Company
-- Oak Ferry Shredding, Storage & Scanning

Description
-- Secure and Affordable Toronto & GTA On-Site Shredding, Document Storage & Scanning Company

Call to Action
-- Get a Quote

Font styles to use
Sans Serif

```html
<!DOCTYPE html>
<html lang="en">
<head>
<meta charset="utf-8">
<title>Oak-Ferry Display Banners</title>
<link rel="stylesheet" href="https://fonts.googleapis.com/css2?family=Bebas+Neue&family=Oswald:wght@400;500&family=Arimo:wght@400&display=swap">
<style>
  :root {
    --canvas-bg: #062a3b;
    --panel-white: #ffffff;
    --panel-grey: #eef0f2;
    --headline-blue: #1f5aa8;
    --frame-blue: #1c62c0;
    --accent-blue: #1a8fe0;
    --accent-green: #17c24f;
    --cta-green: #14bd4c;
    --cta-green-dark: #0fa540;
    --body-ink: #111418;
  }
  * { margin: 0; padding: 0; box-sizing: border-box; }
  html, body { width: 1200px; height: 1200px; overflow: hidden; }
  body { background: var(--canvas-bg); position: relative; }

  .banner {
    position: absolute;
    left: 240px;
    width: 720px;
    height: 273px;
    overflow: hidden;
    background: linear-gradient(100deg, var(--panel-grey) 0%, var(--panel-white) 45%, var(--panel-grey) 100%);
    box-shadow: 0 2px 8px rgba(0,0,0,0.35);
  }
  .banner--storage   { top: 4px; }
  .banner--scanning  { top: 308px; }
  .banner--shredding { top: 614px; }
  .banner--combined  { top: 919px; }

  .banner__art { position: absolute; inset: 0; width: 720px; height: 273px; }

  .banner__copy {
    position: absolute;
    left: 0;
    top: 36px;
    width: 400px;
    text-align: center;
  }
  .banner__headline {
    font-family: "Bebas Neue", "Oswald", sans-serif;
    font-weight: 400;
    font-size: 44px;
    line-height: 42px;
    letter-spacing: 1.5px;
    color: var(--headline-blue);
    white-space: nowrap;
  }
  .banner__text {
    margin-top: 6px;
    font-family: "Oswald", sans-serif;
    font-weight: 400;
    font-size: 17.5px;
    line-height: 19px;
    color: var(--body-ink);
    white-space: nowrap;
  }
  .banner__cta {
    position: absolute;
    left: 93px;
    top: 190px;
    width: 208px;
    height: 48px;
    border-radius: 6px;
    background: linear-gradient(180deg, var(--cta-green) 0%, var(--cta-green-dark) 100%);
    box-shadow: 0 3px 5px rgba(0,0,0,0.3);
    color: #ffffff;
    font-family: "Arimo", sans-serif;
    font-size: 26px;
    line-height: 48px;
    text-align: center;
  }
</style>
</head>
<body>

  <section class="banner banner--storage">
    <svg class="banner__art" viewBox="0 0 720 273" role="img" aria-label="Warehouse aisle of tall blue racking shelves filled with archive boxes">
      <defs>
        <linearGradient id="photo-storage" x1="0" y1="0" x2="1" y2="1">
          <stop offset="0" stop-color="#3a5fa8"/>
          <stop offset="0.5" stop-color="#c9bfae"/>
          <stop offset="1" stop-color="#8a8f96"/>
        </linearGradient>
      </defs>
      <polygon points="0,0 48,0 0,28" fill="var(--accent-green)"/>
      <path d="M432 0 L720 0 L720 260 L398 260 Q380 260 386 244 Z" fill="url(#photo-storage)" stroke="var(--frame-blue)" stroke-width="3"/>
      <polygon points="412,0 454,0 434,26" fill="var(--accent-blue)"/>
      <polygon points="638,273 720,273 720,207" fill="var(--accent-blue)"/>
    </svg>
    <div class="banner__copy">
      <h2 class="banner__headline">Secure<br>Records Storage</h2>
      <p class="banner__text">Local, Affordable Storage Solutions.<br>Protect and Store your Documents in our Secure Facility</p>
    </div>
    <div class="banner__cta">Get a Qoute</div>
  </section>

  <section class="banner banner--scanning">
    <svg class="banner__art" viewBox="0 0 720 273" role="img" aria-label="Hand placing a blue document folder on an open office scanner">
      <defs>
        <linearGradient id="photo-scanning" x1="0" y1="0" x2="1" y2="1">
          <stop offset="0" stop-color="#d9dcdf"/>
          <stop offset="0.5" stop-color="#4a78c0"/>
          <stop offset="1" stop-color="#e6e7e9"/>
        </linearGradient>
      </defs>
      <polygon points="0,0 48,0 0,28" fill="var(--accent-green)"/>
      <path d="M432 0 L720 0 L720 260 L398 260 Q380 260 386 244 Z" fill="url(#photo-scanning)" stroke="var(--frame-blue)" stroke-width="3"/>
      <polygon points="412,0 454,0 434,26" fill="var(--accent-blue)"/>
      <polygon points="638,273 720,273 720,207" fill="var(--accent-blue)"/>
    </svg>
    <div class="banner__copy">
      <h2 class="banner__headline">Document<br>Scanning Services</h2>
      <p class="banner__text">Scan and documents and files with Professional<br>scanning services from Oak-Ferry</p>
    </div>
    <div class="banner__cta">Get a Qoute</div>
  </section>

  <section class="banner banner--shredding">
    <svg class="banner__art" viewBox="0 0 720 273" role="img" aria-label="Hand feeding paper into a secure office shredding console">
      <defs>
        <linearGradient id="photo-shredding" x1="0" y1="0" x2="1" y2="1">
          <stop offset="0" stop-color="#d4d6d8"/>
          <stop offset="0.55" stop-color="#f1f1f0"/>
          <stop offset="1" stop-color="#9fc6e6"/>
        </linearGradient>
      </defs>
      <polygon points="0,0 48,0 0,28" fill="var(--accent-green)"/>
      <path d="M432 0 L720 0 L720 260 L398 260 Q380 260 386 244 Z" fill="url(#photo-shredding)" stroke="var(--frame-blue)" stroke-width="3"/>
      <polygon points="412,0 454,0 434,26" fill="var(--accent-blue)"/>
      <polygon points="638,273 720,273 720,207" fill="var(--accent-blue)"/>
    </svg>
    <div class="banner__copy">
      <h2 class="banner__headline">Secure<br>Shredding Services</h2>
      <p class="banner__text">Certified, Affordable Office Shredding Since 2003.<br>Fast, no contact shredding service</p>
    </div>
    <div class="banner__cta">Get a Qoute</div>
  </section>

  <section class="banner banner--combined">
    <svg class="banner__art" viewBox="0 0 720 273" role="img" aria-label="Uniformed service technician receiving a document box in an office hallway">
      <defs>
        <linearGradient id="photo-combined" x1="0" y1="0" x2="1" y2="1">
          <stop offset="0" stop-color="#b7b3ab"/>
          <stop offset="0.5" stop-color="#8fa3bb"/>
          <stop offset="1" stop-color="#e8e8e8"/>
        </linearGradient>
      </defs>
      <polygon points="0,0 48,0 0,28" fill="var(--accent-green)"/>
      <path d="M432 0 L720 0 L720 260 L398 260 Q380 260 386 244 Z" fill="url(#photo-combined)" stroke="var(--frame-blue)" stroke-width="3"/>
      <polygon points="412,0 454,0 434,26" fill="var(--accent-blue)"/>
      <polygon points="638,273 720,273 720,207" fill="var(--accent-blue)"/>
    </svg>
    <div class="banner__copy">
      <h2 class="banner__headline">Shred, Scan &amp; Store<br>Documents</h2>
      <p class="banner__text">Quick, no contact and affordable paper shredding<br>services in Toronto &amp; Southern Ontario</p>
    </div>
    <div class="banner__cta">Get a Qoute</div>
  </section>

</body>
</html>
```